Company Profile
Korvane Cargo Sdn Bhd is a well-established and experienced freight forwarder in Kuala Lumpur, Malaysia. We specialize in air and sea forwarding, Custom Brokerage and regulatory compliance services, inland transportation, overseas freighting and warehousing and distribution management. With our dedicated qualified and experienced professionals, we are fully committed to serving our clients.

Our Mission
Based on the motto “Quick, Reliable and Polite”, Korvane Cargo is dedicated to upholding the following three points corporate philosophy:1. Adhering to the principle that “the customer always comes first”.2. Contributing to the development of the local community.3. Making it our duty to be responsible and sincere.

Our Edge
• One-Stop Logistics Solutions
• Extensive Network Throughout Malaysia
• Highly Qualified and Experienced Pool of Professionals
• Comprehensive IT Solutions
• Innovative and Customer-focused Solutions
• Flexible and Consistent in Managing Exceptions
• Total Supply Chain Visibility

Target Market : We sell the logistics services to all the industry in Malaysia. (One Stop Logistics Solutions)

Business Card Detail : I would like to see the logo on the front with the general info.

Must Haves :
1) Name, Title, Office, Cell, Fax, Email, Address, Website
2) Must have complete company name show as : Korvane Cargo Sdn Bhd
3) Must have company registration no, show as : 8571620-W

Nice to Haves : Modern Design Business Card

Target Market(s)

We sell the logistics services to all the industry in Malaysia. (One Stop Logistics Solutions)

Contact Information for Business Card

I would like to see the logo on the front with the general info.

Colors

Designer to choose colors to be used in the design.

Requirements
Must have
• 1) Name, Title, Office, Cell, Fax, Email, Address, Website
• 2) Must have complete company name show as : Korvane Cargo Sdn Bhd
• 3) Must have company registration no, show as : 8571620-W
Nice to have
• Modern Design Business Card
Should not have
• Nil

```html
<!DOCTYPE html>
<html lang="en">
<head>
<meta charset="utf-8">
<title>Korvane Cargo – Business Card</title>
<link rel="stylesheet" href="https://fonts.googleapis.com/css2?family=Open+Sans:wght@300;400;600;700&display=swap">
<style>
  :root {
    --bg-light: #f4f4f4;
    --bg-dark: #c9c9c9;
    --card-top: #fbfbfb;
    --card-bottom: #dcdcdc;
    --navy: #0f4a8a;
    --brand-blue: #1f5c99;
    --sky: #2f93cf;
    --sky-light: #5fb2e0;
    --text-grey: #5a5a5a;
    --text-dark: #3a3a3a;
    --panel-grey: #c4c4c4;
  }
  * { margin: 0; padding: 0; box-sizing: border-box; }
  html, body { width: 1200px; height: 1020px; overflow: hidden; }
  body {
    font-family: "Open Sans", Arial, sans-serif;
    background: radial-gradient(ellipse at 50% 35%, var(--bg-light) 0%, #e6e6e6 45%, var(--bg-dark) 100%);
    position: relative;
  }
  .card {
    position: absolute;
    width: 760px;
    height: 434px;
    background: linear-gradient(160deg, var(--card-top) 0%, #ececec 55%, var(--card-bottom) 100%);
    box-shadow: 0 6px 18px rgba(0,0,0,.25);
    overflow: hidden;
  }
  .card-back { left: 90px; top: 60px; }
  .card-front { left: 350px; top: 546px; }
  .card-shapes { position: absolute; inset: 0; width: 100%; height: 100%; }

  .brand { position: absolute; display: flex; align-items: center; gap: 12px; }
  .brand-dot { width: 34px; height: 34px; border-radius: 50%; background: var(--brand-blue); }
  .brand-name { font-weight: 700; font-size: 26px; color: var(--brand-blue); letter-spacing: 1px; white-space: nowrap; }

  /* Back */
  .edge-title { position: absolute; left: 44px; top: 96px; font-size: 16px; color: var(--sky); font-weight: 400; }
  .edge-list { position: absolute; left: 44px; top: 124px; list-style: none; }
  .edge-list li { display: flex; align-items: center; gap: 8px; font-size: 15.5px; color: var(--text-grey); height: 28px; }
  .edge-list svg { width: 16px; height: 14px; flex: none; }
  .card-back .brand { right: 44px; top: 262px; }
  .slogan { position: absolute; right: 50px; top: 340px; font-size: 17px; color: #e9f4fb; }

  /* Front */
  .card-front .brand { left: 40px; top: 46px; }
  .divider { position: absolute; left: 40px; top: 118px; width: 680px; height: 2px; background: linear-gradient(90deg, var(--sky), var(--sky-light)); }
  .holder { position: absolute; right: 60px; top: 170px; text-align: right; }
  .holder-name { font-size: 30px; color: var(--text-dark); font-weight: 300; letter-spacing: 1px; }
  .holder-name b { font-weight: 700; }
  .holder-title { font-size: 17px; color: var(--brand-blue); margin-top: 4px; }
  .holder-bar { width: 210px; height: 4px; background: var(--sky); margin: 8px 0 0 auto; }
  .contacts { position: absolute; left: 40px; top: 170px; list-style: none; }
  .contacts li { display: flex; align-items: center; gap: 10px; font-size: 17px; color: var(--text-dark); height: 26px; }
  .contacts svg { width: 17px; height: 15px; flex: none; }
  .company { position: absolute; left: 40px; top: 358px; font-size: 19px; color: var(--sky-light); }
  .address { position: absolute; left: 40px; top: 386px; font-size: 18px; color: #fff; }
  .reg-no { position: absolute; right: 36px; top: 392px; font-size: 17px; color: #6d7f91; }
</style>
</head>
<body>

<section class="card card-back" aria-label="Business card back">
  <svg class="card-shapes" viewBox="0 0 760 434" preserveAspectRatio="none" aria-hidden="true">
    <defs>
      <linearGradient id="slogan-band" x1="0" x2="1">
        <stop offset="0" stop-color="#1f6fb0"/>
        <stop offset="1" stop-color="#3a9fd6"/>
      </linearGradient>
    </defs>
    <polygon points="400,322 760,322 760,434 372,434" fill="url(#slogan-band)"/>
    <polygon points="0,408 380,408 372,434 0,434" fill="var(--navy)"/>
  </svg>
  <h3 class="edge-title">Our Edge</h3>
  <ul class="edge-list">
    <li><svg viewBox="0 0 16 14"><rect x="1" y="3" width="10" height="10" fill="none" stroke="#1f5c99" stroke-width="1.6"/><path d="M3 8l3 3 9-10" fill="none" stroke="#1f5c99" stroke-width="2"/></svg>One-Stop Logistics Solutions</li>
    <li><svg viewBox="0 0 16 14"><rect x="1" y="3" width="10" height="10" fill="none" stroke="#1f5c99" stroke-width="1.6"/><path d="M3 8l3 3 9-10" fill="none" stroke="#1f5c99" stroke-width="2"/></svg>Extensive Network Throughout Malaysia</li>
    <li><svg viewBox="0 0 16 14"><rect x="1" y="3" width="10" height="10" fill="none" stroke="#1f5c99" stroke-width="1.6"/><path d="M3 8l3 3 9-10" fill="none" stroke="#1f5c99" stroke-width="2"/></svg>Highly Qualified and Experienced Pool of Professionals</li>
    <li><svg viewBox="0 0 16 14"><rect x="1" y="3" width="10" height="10" fill="none" stroke="#1f5c99" stroke-width="1.6"/><path d="M3 8l3 3 9-10" fill="none" stroke="#1f5c99" stroke-width="2"/></svg>Comprehensive IT Solutions</li>
    <li><svg viewBox="0 0 16 14"><rect x="1" y="3" width="10" height="10" fill="none" stroke="#1f5c99" stroke-width="1.6"/><path d="M3 8l3 3 9-10" fill="none" stroke="#1f5c99" stroke-width="2"/></svg>Innovative and Customer-focused Solutions</li>
    <li><svg viewBox="0 0 16 14"><rect x="1" y="3" width="10" height="10" fill="none" stroke="#1f5c99" stroke-width="1.6"/><path d="M3 8l3 3 9-10" fill="none" stroke="#1f5c99" stroke-width="2"/></svg>Flexible and Consistent in Managing Exceptions</li>
    <li><svg viewBox="0 0 16 14"><rect x="1" y="3" width="10" height="10" fill="none" stroke="#1f5c99" stroke-width="1.6"/><path d="M3 8l3 3 9-10" fill="none" stroke="#1f5c99" stroke-width="2"/></svg>Total Supply Chain Visibility</li>
  </ul>
  <div class="brand">
    <span class="brand-dot"></span>
    <span class="brand-name">KORVANE CARGO</span>
  </div>
  <p class="slogan">Quick, Reliable and Polite</p>
</section>

<section class="card card-front" aria-label="Business card front">
  <svg class="card-shapes" viewBox="0 0 760 434" preserveAspectRatio="none" aria-hidden="true">
    <polygon points="0,340 500,340 470,434 0,434" fill="var(--navy)"/>
    <polygon points="500,360 760,360 760,368 497,368" fill="var(--navy)"/>
    <polygon points="497,368 760,368 760,434 470,434" fill="var(--panel-grey)"/>
  </svg>
  <div class="brand">
    <span class="brand-dot"></span>
    <span class="brand-name">KORVANE CARGO</span>
  </div>
  <div class="divider"></div>
  <ul class="contacts">
    <li><svg viewBox="0 0 17 15"><path d="M1 5c0-3 15-3 15 0v2h-4V5H5v2H1z M3 8h11l2 6H1z" fill="#2f93cf"/></svg>000 000 0000</li>
    <li><svg viewBox="0 0 17 15"><rect x="4" y="1" width="9" height="5" fill="none" stroke="#2f93cf" stroke-width="1.5"/><rect x="1" y="6" width="15" height="8" rx="1" fill="#2f93cf"/></svg>000 000 0000</li>
    <li><svg viewBox="0 0 17 15"><rect x="1" y="2" width="15" height="11" fill="#1f5c99"/><path d="M1 2l7.5 6L16 2" fill="none" stroke="#fff" stroke-width="1.4"/></svg>youremail@xyz.com</li>
    <li><svg viewBox="0 0 17 15"><circle cx="8.5" cy="7.5" r="6.5" fill="none" stroke="#2f93cf" stroke-width="1.4"/><ellipse cx="8.5" cy="7.5" rx="3" ry="6.5" fill="none" stroke="#2f93cf" stroke-width="1.1"/><path d="M2 7.5h13" stroke="#2f93cf" stroke-width="1.1"/></svg>www.Website.com</li>
  </ul>
  <div class="holder">
    <p class="holder-name">YOUR <b>NAME</b></p>
    <p class="holder-title">JOB TITLE</p>
    <div class="holder-bar"></div>
  </div>
  <p class="company">Korvane Cargo Sdn Bhd</p>
  <p class="address">Anywhere. Somewhere, St. Name, City 0000</p>
  <p class="reg-no">Reg. No.8571620-W</p>
</section>

</body>
</html>
```